New Property management company business cards

Looking for a new business card, to reflect new younger ownership
Card should be clean, simple and professional but with a modern layout that is conveys our new logo and business model

Key aspects of the business:

Property Management
Facility Maintenance
Project Management
Tenant Improvements

Mailing Address:
PO BOX 7186
Larkfield CA, 95417

Phone: 209-614-8837
Direct: 209-614-8831

Doyle Farrant
President

Target Market(s)

Commercial property owners

Industry/Entity Type

Real Estate property management

Contact Information for Business Card

Open to all designs but lean toward vertical layouts

Requirements
Must have
• Logo and space to customize name and contact info

```html
<!DOCTYPE html>
<html lang="en">
<head>
<meta charset="utf-8">
<title>Norvale Property Management – Business Card</title>
<link rel="stylesheet" href="https://fonts.googleapis.com/css2?family=Lexend:wght@300;400;500;700&display=swap">
<style>
  :root {
    --backdrop: #d7d7d7;
    --navy: #23253a;
    --teal: #2fbfae;
    --white: #ffffff;
    --ink: #23253a;
  }
  * { box-sizing: border-box; margin: 0; padding: 0; }
  html, body {
    width: 1200px; height: 1200px; overflow: hidden;
    background: var(--backdrop);
    font-family: "Lexend", "Helvetica Neue", Arial, sans-serif;
  }
  .canvas { position: relative; width: 1200px; height: 1200px; }
  .card {
    position: absolute; top: 250px;
    width: 390px; height: 682px;
    overflow: hidden;
    box-shadow: 0 18px 40px rgba(0,0,0,0.18);
  }
  .card--front { left: 150px; background: var(--navy); color: var(--white); }
  .card--back  { left: 660px; background: var(--white); color: var(--ink); }

  .wordmark {
    position: absolute; left: 0; right: 0; top: 140px;
    text-align: center; font-weight: 500;
  }
  .wordmark__mark {
    display: block; width: 22px; height: 22px; margin: 0 auto 22px;
    background: var(--teal);
  }
  .wordmark__name {
    display: block; font-size: 44px; letter-spacing: 6px; line-height: 1;
  }
  .wordmark__tag {
    display: block; font-size: 12px; letter-spacing: 6px; margin-top: 10px;
  }
  .card--front .wordmark { color: var(--white); }
  .card--back .wordmark { color: var(--navy); top: 110px; }

  .services {
    position: absolute; left: 0; right: 0; top: 360px;
    list-style: none; text-align: center;
    font-size: 21px; font-weight: 400; line-height: 1.4;
  }
  .front-band {
    position: absolute; left: 0; right: 0; bottom: 0; height: 10px;
    background: var(--teal);
  }

  .contact { position: absolute; left: 46px; right: 24px; top: 330px; }
  .contact__name {
    color: var(--teal); font-weight: 700; font-size: 31px;
    letter-spacing: 0.5px; text-transform: uppercase; line-height: 1.2;
  }
  .contact__role { font-size: 22px; font-weight: 400; margin-top: 2px; }
  .contact__address { font-size: 21px; line-height: 1.35; margin-top: 26px; }
  .contact__list { list-style: none; margin-top: 14px; font-size: 21px; line-height: 1.45; }
  .contact__list li { display: flex; align-items: center; gap: 10px; white-space: nowrap; }
  .contact__list svg { width: 17px; height: 17px; flex: none; fill: var(--teal); }
</style>
</head>
<body>
<main class="canvas">
  <section class="card card--front" aria-label="Card front">
    <div class="wordmark">
      <span class="wordmark__mark"></span>
      <span class="wordmark__name">NORVALE</span>
      <span class="wordmark__tag">PROPERTY MANAGEMENT</span>
    </div>
    <ul class="services">
      <li>Property Management</li>
      <li>Facility Maintenance</li>
      <li>Project Management</li>
      <li>Tenant Improvements</li>
    </ul>
    <div class="front-band"></div>
  </section>

  <section class="card card--back" aria-label="Card back">
    <div class="wordmark">
      <span class="wordmark__mark"></span>
      <span class="wordmark__name">NORVALE</span>
      <span class="wordmark__tag">PROPERTY MANAGEMENT</span>
    </div>
    <div class="contact">
      <h1 class="contact__name">Doyle Farrant</h1>
      <p class="contact__role">President</p>
      <p class="contact__address">PO BOX 7186<br>Larkfield CA, 95417</p>
      <ul class="contact__list">
        <li><svg viewBox="0 0 24 24" aria-hidden="true"><path d="M6.6 10.8a15 15 0 0 0 6.6 6.6l2.2-2.2c.3-.3.7-.4 1-.2 1.1.4 2.3.6 3.6.6.6 0 1 .4 1 1V20c0 .6-.4 1-1 1A17 17 0 0 1 3 4c0-.6.4-1 1-1h3.5c.6 0 1 .4 1 1 0 1.3.2 2.5.6 3.6.1.3 0 .7-.2 1z"/></svg>209-614-8837</li>
        <li><svg viewBox="0 0 24 24" aria-hidden="true"><path d="M7 1h10a2 2 0 0 1 2 2v18a2 2 0 0 1-2 2H7a2 2 0 0 1-2-2V3a2 2 0 0 1 2-2zm0 3v14h10V4zm5 15.5a1 1 0 1 0 0 2 1 1 0 0 0 0-2z"/></svg>209-614-8831</li>
        <li><svg viewBox="0 0 24 24" aria-hidden="true"><path d="M2 5h20v2l-10 6L2 7zm0 4 10 6 10-6v10H2z"/></svg>doyle@norvalepm.com</li>
        <li><svg viewBox="0 0 24 24" aria-hidden="true"><path d="M12 2a10 10 0 1 0 0 20 10 10 0 0 0 0-20zm0 2c1 0 2.2 1.8 2.7 5H9.3C9.8 5.8 11 4 12 4zm-7.7 7h3c0 .7 0 1.4.1 2h-3a8 8 0 0 1-.1-2zm5 0h5.4a19 19 0 0 1 0 2H9.3a19 19 0 0 1 0-2zm7.4 0h3a8 8 0 0 1 0 2h-3.1c.1-.6.1-1.3.1-2zM9.3 15h5.4c-.5 3.2-1.7 5-2.7 5s-2.2-1.8-2.7-5z"/></svg>www.norvalepm.com</li>
      </ul>
    </div>
  </section>
</main>
</body>
</html>
```